KEM Infographic that describes my Software Product

I am looking for an infographic that describes a software tool that I want to market to prospective clients .. the infographic will consist of about 8 steps .. The tool is used by a business to automate their business processes .. the general flow is to define the process in a series of steps with each step having rules about what role does the step and what is the outcome of the step [outcome can be sending a text message to a client as an example] .. once the process / steps are defined then the solution helps the business track / standardize how the process gets executed

Target Market(s)

Small to mid-sized business who use Velbrook Quantilis CRM

Font styles to use
Sans Serif

Colors
85acd3
33a6d7

Requirements
Must have
• Clearly defined sequence of steps that describes how the software tool works .. I will provide definition of what hose steps are.

```html
<!DOCTYPE html>
<html lang="en">
<head>
<meta charset="utf-8">
<title>Infographic</title>
<link rel="stylesheet" href="https://fonts.googleapis.com/css2?family=Montserrat:wght@300;400;600;700&display=swap">
<style>
  :root {
    --frame: #d1d3d4;
    --paper: #f3f3f4;
    --map: #e4e5e6;
    --ink: #4a4a4c;
    --ring: #58585a;
    --brand: #1fa3c9;
    --c1: #fcc70f; --c1-arc: #f5b31a;
    --c2: #f9a51b; --c2-arc: #f68c1f;
    --c3: #ea4f3d; --c3-arc: #e6413a;
    --c4: #1fa3c9; --c4-arc: #1a9ec4;
    --c5: #1e9c8c; --c5-arc: #168f80;
    --c6: #4fa846; --c6-arc: #3f9c3c;
    --c7: #86b83c; --c7-arc: #78ad36;
    --c8: #bccd2e; --c8-arc: #a9c233;
  }
  * { box-sizing: border-box; margin: 0; padding: 0; }
  html, body { width: 850px; height: 1200px; overflow: hidden; }
  body { background: var(--frame); font-family: "Montserrat", Arial, sans-serif; position: relative; }
  .sheet { position: absolute; left: 24px; top: 24px; width: 802px; height: 1152px; background: var(--paper); overflow: hidden; }
  .world-map {
    position: absolute; left: 10px; top: 320px; width: 782px; height: 690px;
    background: radial-gradient(ellipse at 50% 45%, var(--map) 0%, rgba(228,229,230,0.6) 55%, rgba(243,243,244,0) 80%);
  }
  .graphics { position: absolute; left: -24px; top: -24px; width: 850px; height: 1200px; }
  .badge-text {
    position: absolute; left: 204px; top: 71px; width: 398px; height: 62px;
    display: flex; align-items: center; justify-content: center;
    color: #fff; font-size: 44px; font-weight: 400; letter-spacing: 0.5px;
  }
  .title {
    position: absolute; left: 0; top: 205px; width: 802px; text-align: center;
    color: var(--ink); font-size: 43px; font-weight: 700; line-height: 50px;
  }
  .step { position: absolute; width: 166px; }
  .step-label { font-size: 21px; color: var(--ink); white-space: nowrap; letter-spacing: -0.2px; }
  .step-label .num { font-weight: 300; }
  .step-label .key { font-weight: 600; }
  .step-label .rest { font-weight: 700; }
  .step-text {
    margin-top: 8px; font-size: 9.4px; font-weight: 600; line-height: 13px;
    color: #58585a; text-align: justify; text-align-last: left;
  }
  .s1 .key { color: var(--c1-arc); } .s2 .key { color: var(--c2-arc); }
  .s3 .key { color: var(--c3); }     .s4 .key { color: var(--c4); }
  .s5 .key { color: var(--c5); }     .s6 .key { color: var(--c6); }
  .s7 .key { color: var(--c7); }     .s8 .key { color: var(--c8-arc); }
</style>
</head>
<body>
<div class="sheet">
  <div class="world-map" role="img" aria-label="Faint world map in the background"></div>

  <svg class="graphics" viewBox="0 0 850 1200" aria-hidden="true">
    <defs>
      <filter id="lift" x="-30%" y="-30%" width="160%" height="160%">
        <feDropShadow dx="3" dy="4" stdDeviation="3" flood-color="#000" flood-opacity="0.22"/>
      </filter>
    </defs>

    <path d="M232 128 A88 70 0 0 1 320 56 L534 56 A88 70 0 0 1 622 128" fill="none" stroke="var(--brand)" stroke-width="8"/>
    <path d="M222 128 A96 68 0 0 0 318 194 L536 194 A96 68 0 0 0 632 128" fill="none" stroke="var(--ring)" stroke-width="2.5"/>
    <circle cx="210" cy="126" r="7" fill="var(--ring)"/>
    <circle cx="644" cy="126" r="7" fill="var(--ring)"/>
    <rect x="228" y="95" width="398" height="62" rx="31" fill="var(--brand)" filter="url(#lift)"/>

    <g fill="var(--ring)">
      <circle cx="239" cy="467" r="7"/><circle cx="431" cy="467" r="7"/><circle cx="622" cy="467" r="7"/>
      <circle cx="239" cy="871" r="7"/><circle cx="431" cy="871" r="7"/><circle cx="622" cy="871" r="7"/>
    </g>

    <g fill="none" stroke="var(--ring)" stroke-width="2.5">
      <circle cx="142" cy="467" r="81"/><circle cx="335" cy="467" r="81"/>
      <circle cx="527" cy="467" r="81"/><circle cx="719" cy="467" r="81"/>
      <circle cx="142" cy="871" r="81"/><circle cx="335" cy="871" r="81"/>
      <circle cx="527" cy="871" r="81"/><circle cx="719" cy="871" r="81"/>
    </g>

    <g fill="none" stroke-width="13">
      <circle cx="142" cy="467" r="75" stroke="var(--c1-arc)" stroke-dasharray="239 500" transform="rotate(45 142 467)"/>
      <circle cx="335" cy="467" r="75" stroke="var(--c2-arc)" stroke-dasharray="239 500" transform="rotate(-45 335 467)"/>
      <circle cx="527" cy="467" r="75" stroke="var(--c3-arc)" stroke-dasharray="262 500" transform="rotate(-8 527 467)"/>
      <circle cx="719" cy="467" r="75" stroke="var(--c4-arc)" stroke-dasharray="280 500" transform="rotate(150 719 467)"/>
      <circle cx="142" cy="871" r="75" stroke="var(--c5-arc)" stroke-dasharray="225 500" transform="rotate(60 142 871)"/>
      <circle cx="335" cy="871" r="75" stroke="var(--c6-arc)" stroke-dasharray="262 500" transform="rotate(100 335 871)"/>
      <circle cx="527" cy="871" r="75" stroke="var(--c7-arc)" stroke-dasharray="239 500" transform="rotate(-45 527 871)"/>
      <circle cx="719" cy="871" r="75" stroke="var(--c8-arc)" stroke-dasharray="252 500" transform="rotate(170 719 871)"/>
    </g>

    <g filter="url(#lift)">
      <circle cx="142" cy="467" r="60" fill="var(--c1)"/><circle cx="335" cy="467" r="60" fill="var(--c2)"/>
      <circle cx="527" cy="467" r="60" fill="var(--c3)"/><circle cx="719" cy="467" r="60" fill="var(--c4)"/>
      <circle cx="142" cy="871" r="60" fill="var(--c5)"/><circle cx="335" cy="871" r="60" fill="var(--c6)"/>
      <circle cx="527" cy="871" r="60" fill="var(--c7)"/><circle cx="719" cy="871" r="60" fill="var(--c8)"/>
    </g>

    <g fill="none" stroke="#fff" stroke-width="2.2" stroke-linecap="round" stroke-linejoin="round">
      <g transform="translate(142 467)">
        <path d="M-8 10 C-8 2 -16 -2 -16 -10 A16 16 0 0 1 16 -10 C16 -2 8 2 8 10 Z"/>
        <path d="M-7 14 H7 M-6 18 H6 M-3 22 H3"/>
        <path d="M0 -33 V-28 M-22 -25 L-19 -22 M22 -25 L19 -22 M-28 -10 H-24 M28 -10 H24"/>
      </g>
      <g transform="translate(335 467)">
        <rect x="-15" y="0" width="8" height="20"/><rect x="-4" y="-8" width="8" height="28"/><rect x="7" y="-4" width="8" height="24"/>
        <path d="M-20 20 H20 M-18 -10 L-6 -20 L4 -14 L18 -26"/>
        <circle cx="-18" cy="-10" r="2.5"/><circle cx="-6" cy="-20" r="2.5"/><circle cx="4" cy="-14" r="2.5"/><circle cx="18" cy="-26" r="2.5"/>
      </g>
      <g transform="translate(527 467)">
        <rect x="-24" y="-20" width="48" height="32" rx="2"/>
        <path d="M-6 12 L-8 20 H8 L6 12 M-12 20 H12 M-24 6 H24"/>
        <circle cx="0" cy="-4" r="5"/><path d="M0 -13 V-10 M0 2 V5 M-9 -4 H-6 M6 -4 H9 M-6 -10 L-4 -8 M6 -10 L4 -8"/>
      </g>
      <g transform="translate(719 467)">
        <circle cx="-5" cy="-5" r="14"/><circle cx="-5" cy="-5" r="10"/>
        <path d="M5 5 L20 20" stroke-width="5"/>
      </g>
      <g transform="translate(142 871)">
        <rect x="-6" y="-24" width="30" height="20"/><path d="M-6 -24 L9 -13 L24 -24"/>
        <rect x="-26" y="-2" width="30" height="20"/><path d="M-26 -2 L-11 9 L4 -2 M-26 18 L-15 8 M4 18 L-7 8"/>
        <path d="M-26 -18 H-12 M-22 -22 L-26 -18 L-22 -14 M10 8 H24 M20 4 L24 8 L20 12"/>
      </g>
      <g transform="translate(335 871)">
        <circle r="24"/><ellipse rx="10" ry="24"/><path d="M-24 0 H24 M-20 -12 H20 M-20 12 H20 M0 -24 V24"/>
      </g>
      <g transform="translate(527 871)">
        <path d="M-16 -26 H8 L16 -18 V22 H-16 Z M8 -26 V-18 H16"/>
        <path d="M-10 -14 H4 M-10 -8 H10 M-10 -2 H10 M-10 4 H10"/>
        <circle cx="6" cy="14" r="4"/><path d="M3 17 L1 26 L6 23 L11 26 L9 17"/>
      </g>
      <g transform="translate(719 871)">
        <path d="M-12 -24 H12 L18 -16 L0 4 L-18 -16 Z M-18 -16 H18 M-6 -24 L-8 -16 L0 4 L8 -16 L6 -24"/>
        <path d="M-26 14 L-14 8 C-8 6 -2 10 4 12 H10 C12 12 12 16 10 16 H-2 M-26 24 L-18 20 H6 L24 8 C26 6 24 2 20 4 L10 12"/>
      </g>
    </g>
  </svg>

  <div class="badge-text">INFOGRAPHIC</div>
  <h1 class="title">Lorem Ipsum<br>Dolor Sit Amet</h1>

  <div class="step s1" style="left:40px;top:558px">
    <p class="step-label"><span class="num">1. </span><span class="key">lorem</span> <span class="rest">ipsum</span></p>
    <p class="step-text">Lorem ipsum dolor sit amet, consectetur adipiscing elit, sed do eiusmod tempor incididunt ut labore et dolore magna aliqua</p>
  </div>
  <div class="step s2" style="left:233px;top:558px">
    <p class="step-label"><span class="num">2. </span><span class="key">lorem</span> <span class="rest">ipsum</span></p>
    <p class="step-text">Lorem ipsum dolor sit amet, consectetur adipiscing elit, sed do eiusmod tempor incididunt ut labore et dolore magna aliqua</p>
  </div>
  <div class="step s3" style="left:425px;top:558px">
    <p class="step-label"><span class="num">3. </span><span class="key">lorem</span> <span class="rest">ipsum</span></p>
    <p class="step-text">Lorem ipsum dolor sit amet, consectetur adipiscing elit, sed do eiusmod tempor incididunt ut labore et dolore magna aliqua</p>
  </div>
  <div class="step s4" style="left:617px;top:558px">
    <p class="step-label"><span class="num">4. </span><span class="key">lorem</span> <span class="rest">ipsum</span></p>
    <p class="step-text">Lorem ipsum dolor sit amet, consectetur adipiscing elit, sed do eiusmod tempor incididunt ut labore et dolore magna aliqua</p>
  </div>
  <div class="step s5" style="left:40px;top:963px">
    <p class="step-label"><span class="num">5. </span><span class="key">lorem</span> <span class="rest">ipsum</span></p>
    <p class="step-text">Lorem ipsum dolor sit amet, consectetur adipiscing elit, sed do eiusmod tempor incididunt ut labore et dolore magna aliqua</p>
  </div>
  <div class="step s6" style="left:233px;top:963px">
    <p class="step-label"><span class="num">6. </span><span class="key">lorem</span> <span class="rest">ipsum</span></p>
    <p class="step-text">Lorem ipsum dolor sit amet, consectetur adipiscing elit, sed do eiusmod tempor incididunt ut labore et dolore magna aliqua</p>
  </div>
  <div class="step s7" style="left:425px;top:963px">
    <p class="step-label"><span class="num">7. </span><span class="key">lorem</span> <span class="rest">ipsum</span></p>
    <p class="step-text">Lorem ipsum dolor sit amet, consectetur adipiscing elit, sed do eiusmod tempor incididunt ut labore et dolore magna aliqua</p>
  </div>
  <div class="step s8" style="left:617px;top:963px">
    <p class="step-label"><span class="num">8. </span><span class="key">lorem</span> <span class="rest">ipsum</span></p>
    <p class="step-text">Lorem ipsum dolor sit amet, consectetur adipiscing elit, sed do eiusmod tempor incididunt ut labore et dolore magna aliqua</p>
  </div>
</div>
</body>
</html>
```